Glenvora pond linings website template

We need a template for our new website. Glenvora is currently marketed through www.sheetvale.com.au, and we are moving the pond/dam linings to a dedicated site www.glenvora.com.au

The site is essentially brochureware. The content (less landing page & photo gallery) is on the new site to give you a better idea of what we do. We are also on Facebook.com/glenvora

We are looking for a template/style which we can adapt to the different sections of the site as required. We also get a lot of phone/tablet visitors so an alternative mobile layout would be a bonus, but by no means required.

I am proficient in HTML/CSS & javascript so can code most designs thrown at me.

Any icons or interface fonts should be freely available web fonts where possible.

Target Market(s)

We are targeting both landscape professionals (design & construction) as well as the DIY market for ponds/wateragrdens.

Industry/Entity Type

Moving

Requirements
Must have
• We need a design (preferably layered PSD or AI) as basis for our overall site look and feel. Fonts/iconography/layout are where we are lacking. We can do the HTML/CSS/JS/PHP internally.
Nice to have
• A style guide either in file or separate would be nice.
Layers with effect (i.e.. :hover, CSS3 transition endpoints, etc)

```html
<!DOCTYPE html>
<html lang="en">
<head>
<meta charset="utf-8">
<title>Glenvora — Pond Linings</title>
<link rel="stylesheet" href="https://fonts.googleapis.com/css2?family=Bebas+Neue&family=Raleway:wght@300;400;600&family=Roboto:wght@400&display=swap">
<style>
  :root {
    --header-wood: #24160d;
    --header-wood-dark: #160d07;
    --nav-text: #f7f3dc;
    --nav-underline: #f2e07a;
    --panel-bg: rgba(8, 10, 12, 0.82);
    --card-bg: #1b1c1e;
    --panel-title: #f2f2f2;
    --panel-text: #c9c9c9;
    --arrow-bg: #c9c76a;
    --arrow-icon: #ffffff;
    --brand-green: #2f6b3c;
    --brand-lime: #b7cc2e;
    --sky-text: #1a1a1a;
  }
  * { box-sizing: border-box; margin: 0; padding: 0; }
  html, body { width: 1200px; height: 900px; overflow: hidden; background: #ffffff; }
  .page { position: relative; width: 1200px; height: 900px; overflow: hidden; font-family: "Roboto", Arial, sans-serif; }

  .top-backdrop {
    position: absolute; left: 0; top: 0; width: 1200px; height: 147px;
    background: linear-gradient(100deg, #3d4a3a 0%, #6c7a6e 18%, #8d9399 40%, #a7abb0 60%, #c9cbcd 80%, #dcdcdc 100%);
  }
  .top-shapes { position: absolute; left: 0; top: 0; }
  .section-label {
    position: absolute; left: 985px; top: 26px;
    font-family: "Raleway", Arial, sans-serif; font-weight: 400; font-size: 29px;
    color: var(--sky-text); letter-spacing: 0.5px;
  }

  .site-header {
    position: absolute; left: 0; top: 147px; width: 1200px; height: 181px;
    background:
      repeating-linear-gradient(90deg, rgba(255,255,255,0.025) 0 3px, rgba(0,0,0,0.05) 3px 9px, rgba(255,255,255,0.02) 9px 14px),
      linear-gradient(180deg, var(--header-wood) 0%, #2c1b10 50%, var(--header-wood-dark) 100%);
  }
  .brand {
    position: absolute; left: 54px; top: 0; width: 169px; height: 181px; background: #ffffff;
  }
  .brand-mark { position: absolute; left: 9px; top: 20px; width: 26px; height: 26px; background: var(--brand-lime); }
  .brand-name {
    position: absolute; left: 9px; top: 56px;
    font-family: "Raleway", Arial, sans-serif; font-weight: 600; font-size: 27px;
    color: var(--brand-green); letter-spacing: 0.5px;
  }
  .main-nav a {
    position: absolute; top: 116px; height: 53px;
    font-family: "Bebas Neue", Impact, sans-serif; font-size: 33px; line-height: 1;
    color: var(--nav-text); text-decoration: none; letter-spacing: 0.5px;
    border-bottom: 3px solid var(--nav-underline); white-space: nowrap;
  }

  .hero {
    position: absolute; left: 0; top: 328px; width: 1200px; height: 572px;
    background:
      radial-gradient(ellipse at 72% 55%, #4b7d93 0%, rgba(40,80,100,0.6) 25%, transparent 50%),
      radial-gradient(ellipse at 10% 60%, #3e5a2c 0%, transparent 45%),
      radial-gradient(ellipse at 50% 15%, #4c5557 0%, transparent 45%),
      linear-gradient(180deg, #262d2a 0%, #1c2a26 50%, #173345 100%);
  }
  .hero-shapes { position: absolute; left: 0; top: 328px; }

  .text-panel {
    position: absolute; width: 253px; padding: 36px 13px 0 13px; background: var(--panel-bg);
  }
  .text-panel.first { left: 159px; top: 383px; height: 451px; }
  .text-panel.second { left: 521px; top: 391px; height: 451px; }
  .panel-title {
    font-family: "Raleway", Arial, sans-serif; font-weight: 300; font-size: 22px;
    color: var(--panel-title); letter-spacing: 1px; margin-bottom: 28px;
  }
  .panel-text {
    font-size: 12.5px; line-height: 21.6px; color: var(--panel-text);
    text-align: justify; word-spacing: 1px; margin-bottom: 9px;
  }

  .photo-card { position: absolute; left: 859px; width: 201px; height: 200px; background: var(--card-bg); }
  .photo-card.upper { top: 392px; }
  .photo-card.lower { top: 642px; }
  .photo-card .photo { position: absolute; left: 6px; width: 191px; height: 127px; }
  .photo-card.upper .photo { top: 39px; background: linear-gradient(180deg, #3f6a3a 0%, #2b4a2c 45%, #1c2b22 70%, #3b4d4a 100%); }
  .photo-card.lower .photo { top: 37px; background: linear-gradient(180deg, #3a5a30 0%, #5d6a55 45%, #6b7270 65%, #2d3f2c 100%); }

  .slider-arrow {
    position: absolute; top: 563px; width: 54px; height: 54px; border-radius: 50%;
    background: var(--arrow-bg); display: flex; align-items: center; justify-content: center;
  }
  .slider-arrow.prev { left: 53px; }
  .slider-arrow.next { left: 1119px; }
</style>
</head>
<body>
<div class="page">
  <div class="top-backdrop" role="img" aria-label="Blurred photograph of garden trees against the sky"></div>
  <svg class="top-shapes" width="1200" height="147" viewBox="0 0 1200 147" aria-hidden="true">
    <polygon points="420,0 640,0 520,147 300,147" fill="#ffffff" fill-opacity="0.12"/>
    <polygon points="650,0 890,0 770,147 520,147" fill="#ffffff" fill-opacity="0.18"/>
    <polygon points="890,0 1200,0 1200,147 770,147" fill="#ffffff"/>
  </svg>
  <div class="section-label">content</div>

  <header class="site-header">
    <div class="brand">
      <span class="brand-mark"></span>
      <span class="brand-name">Glenvora</span>
    </div>
    <nav class="main-nav">
      <a href="#" style="left:247px;width:60px;">HOME</a>
      <a href="#" style="left:349px;width:100px;">ABOUT US</a>
      <a href="#" style="left:469px;width:92px;">GALLERY</a>
      <a href="#" style="left:586px;width:134px;">HAPPENINGS</a>
      <a href="#" style="left:737px;width:143px;">LINER STYLES</a>
      <a href="#" style="left:892px;width:146px;top:114px;">INSTALLATION</a>
      <a href="#" style="left:1055px;width:126px;top:114px;">CONTACT US</a>
    </nav>
  </header>

  <div class="hero" role="img" aria-label="Blurred photograph of a garden pond beside a timber deck and house"></div>
  <svg class="hero-shapes" width="1200" height="572" viewBox="0 0 1200 572" aria-hidden="true">
    <polygon points="0,0 370,0 0,470" fill="#000000" fill-opacity="0.18"/>
    <polygon points="830,572 1200,150 1200,572" fill="#ffffff" fill-opacity="0.08"/>
    <line x1="1010" y1="572" x2="1200" y2="330" stroke="#ffffff" stroke-opacity="0.8" stroke-width="3"/>
  </svg>

  <section class="text-panel first">
    <h2 class="panel-title">TITLE</h2>
    <p class="panel-text">carjgbdrngrdn sujnb naonar nio nio anrdignrsdjna n iadr snionr ia nirn rinsd rd sn.rurh u rouoqd or marngnrdaj gnio ajaidr nir dr guiorgnvaslnbvaun nr raon orui</p>
    <p class="panel-text">aron, adrhgurda u uadngurphj vvg gjnrangu rdhnaurnghuoadpdnn dang ouion adrogi dnraogn dangr roorang ongadngogrgrion daniogrngrndagioadr uoiado raog nadrog nruoangd ordag odnrv jgerdng iodagriogjr ioadnio gkadngio anrmo inadrio niorns non arngioa nioganio nadr iorng aiodnr iogran rna iongioan iong ia</p>
  </section>

  <section class="text-panel second">
    <h2 class="panel-title">TITLE</h2>
    <p class="panel-text">carjgbdrngrdn sujnb naonar nio nio anrdignrsdjna n iadr snionr ia nirn rinsd rd sn.rurh u rouoqd or marngnrdaj gnio ajaidr nir dr guiorgnvaslnbvaun nr raon orui</p>
    <p class="panel-text">aron, adrhgurda u uadngurphj vvg gjnrangu rdhnaurnghuoadpdnn dang ouion adrogi dnraogn dangr roorang ongadngogrgrion daniogrngrndagioadr uoiado raog nadrog nruoangd ordag odnrv jgerdng iodagriogjr ioadnio gkadngio anrmo inadrio niorns non arngioa nioganio nadr iorng aiodnr iogran rna iongioan iong ia</p>
  </section>

  <figure class="photo-card upper">
    <div class="photo" role="img" aria-label="Photograph of a natural rock pond surrounded by ferns"></div>
  </figure>
  <figure class="photo-card lower">
    <div class="photo" role="img" aria-label="Photograph of a small waterfall over boulders into a garden pond"></div>
  </figure>

  <a class="slider-arrow prev" href="#" aria-label="Previous">
    <svg width="14" height="14" viewBox="0 0 14 14"><polyline points="9,2 4,7 9,12" fill="none" stroke="var(--arrow-icon)" stroke-width="2.4"/></svg>
  </a>
  <a class="slider-arrow next" href="#" aria-label="Next">
    <svg width="14" height="14" viewBox="0 0 14 14"><polyline points="5,2 10,7 5,12" fill="none" stroke="var(--arrow-icon)" stroke-width="2.4"/></svg>
  </a>
</div>
</body>
</html>
```